Billboard for a Contractor in Minnesota

Creating our first billboard that will be displayed on a freeway. Will be used on a digital Glint Signboard. Sign should be a 846 x 234 design. Our website is kestrel-paving.com Looking for something specific to "Look us up" or "Call" for your free concrete & asphalt estimate. Needs both web addresses (kestrel-paving.com and kestrel-masonry.com. Needs our phone number, logo. Our slogan is Serving All Your Asphalt & Concrete Needs. It's also our 25 Anniversary.

Target Market(s)

Residential Homeowners in the Twin Cities

Colors
abd036

Requirements
Must have
• Logo, Phone Number, Our Services, Web Addresses (both) Our services are all on our website. (Asphalt Driveway, Concrete Driveway, Concrete Apron, Concrete Sidewalk, Concrete Patio. Colors should be same as website. Black, White, Gray and the Neon Green color.

```html
<!DOCTYPE html>
<html lang="en">
<head>
<meta charset="utf-8">
<title>Kestrel Paving &amp; Masonry – Billboard</title>
<link rel="stylesheet" href="https://fonts.googleapis.com/css2?family=Roboto:wght@400;700;900&family=Roboto+Condensed:wght@700&display=swap">
<style>
  :root {
    --green: #6cbf3f;
    --green-neon: #abd036;
    --blue: #1f5e82;
    --black: #111111;
    --white: #ffffff;
    --grey-text: #1a1a1a;
    --stage: #e9ecef;
  }
  * { margin: 0; padding: 0; box-sizing: border-box; }
  html, body { width: 1200px; height: 749px; overflow: hidden; background: var(--stage); }
  .billboard {
    position: absolute; left: 20px; top: 214px;
    width: 1160px; height: 321px; overflow: hidden;
    font-family: "Roboto", Arial, sans-serif;
  }
  .billboard__art { position: absolute; inset: 0; }
  .slogan {
    position: absolute; left: 548px; top: 12px; width: 600px;
    color: var(--white); font-weight: 900; font-size: 39px; line-height: 1.08;
    text-transform: uppercase; letter-spacing: 0.3px; white-space: nowrap;
  }
  .call {
    position: absolute; left: 580px; top: 112px;
    color: var(--white); font-family: "Roboto Condensed", Arial, sans-serif;
    font-weight: 700; font-size: 28px; letter-spacing: 0.3px; white-space: nowrap;
  }
  .call__number { margin-left: 8px; }
  .brand {
    position: absolute; left: 420px; top: 204px; width: 140px;
    text-align: center; color: var(--black); font-weight: 900;
    font-size: 22px; line-height: 1.1; text-transform: uppercase;
  }
  .services__title {
    position: absolute; left: 640px; top: 186px;
    font-family: "Roboto Condensed", Arial, sans-serif; font-weight: 700;
    color: var(--blue); font-size: 26px; line-height: 30px;
    border-bottom: 2px solid var(--black);
  }
  .services__list {
    position: absolute; list-style: none;
  }
  .services__list--left { left: 640px; top: 222px; }
  .services__list--right { left: 925px; top: 190px; }
  .services__list li {
    display: flex; align-items: center; gap: 8px;
    height: 26px; font-size: 18px; color: var(--grey-text); white-space: nowrap;
  }
  .services__list--right li { font-size: 19px; }
  .services__icon { width: 15px; height: 15px; flex: none; }
  .web {
    position: absolute; left: 650px; top: 295px;
    color: var(--white); font-weight: 700; font-size: 17px; letter-spacing: 0.3px; white-space: nowrap;
  }
</style>
</head>
<body>
  <section class="billboard" aria-label="Kestrel Paving &amp; Masonry billboard">
    <svg class="billboard__art" width="1160" height="321" viewBox="0 0 1160 321">
      <defs>
        <linearGradient id="photoTones" x1="0" y1="0" x2="0" y2="1">
          <stop offset="0" stop-color="#5f7d52"/>
          <stop offset="0.35" stop-color="#8e97a0"/>
          <stop offset="0.6" stop-color="#c7c9c2"/>
          <stop offset="1" stop-color="#dcdcd8"/>
        </linearGradient>
      </defs>
      <rect class="panel-green" width="1160" height="321" fill="var(--green)"/>
      <path class="swoosh-blue" d="M280 321 C330 200 420 70 540 0 L585 0 C465 70 375 200 320 321 Z" fill="var(--blue)"/>
      <path class="swoosh-black" d="M345 321 C395 200 485 70 605 0 L635 0 C515 70 425 200 372 321 Z" fill="var(--black)"/>
      <g role="img" aria-label="Photo of a grey suburban house with a fresh concrete driveway">
        <path d="M0 0 L540 0 C420 70 330 200 280 321 L0 321 Z" fill="url(#photoTones)"/>
      </g>
      <g role="img" aria-label="25th anniversary seal">
        <circle cx="134" cy="228" r="62" fill="#2f8a4e" stroke="#9a8f94" stroke-width="8"/>
      </g>
      <polygon class="call-band" points="562,108 965,100 945,150 545,156" fill="var(--blue)"/>
      <polygon class="services-edge" points="575,186 1080,150 1160,150 1160,170 590,200" fill="var(--black)"/>
      <polygon class="services-panel" points="588,196 1160,164 1160,286 612,290" fill="var(--white)"/>
      <polygon class="web-strip" points="612,288 1160,282 1160,321 620,321" fill="var(--blue)"/>
      <circle cx="638" cy="305" r="5" fill="var(--white)"/>
    </svg>

    <h1 class="slogan">Serving all your asphalt<br>&amp; concrete needs</h1>
    <p class="call">Call us Today!<span class="call__number">612 - 555 - 0187</span></p>

    <p class="brand">Kestrel<br>Paving &amp;<br>Masonry</p>

    <h2 class="services__title">Our Services</h2>
    <ul class="services__list services__list--left">
      <li><svg class="services__icon" viewBox="0 0 16 16"><circle cx="8" cy="8" r="7" fill="none" stroke="var(--blue)" stroke-width="1.5"/><path d="M6.5 4.5 L10 8 L6.5 11.5" fill="none" stroke="var(--blue)" stroke-width="2"/></svg>Asphalt Driveway</li>
      <li><svg class="services__icon" viewBox="0 0 16 16"><circle cx="8" cy="8" r="7" fill="none" stroke="var(--blue)" stroke-width="1.5"/><path d="M6.5 4.5 L10 8 L6.5 11.5" fill="none" stroke="var(--blue)" stroke-width="2"/></svg>Concrete Driveway</li>
    </ul>
    <ul class="services__list services__list--right">
      <li><svg class="services__icon" viewBox="0 0 16 16"><circle cx="8" cy="8" r="7" fill="none" stroke="var(--blue)" stroke-width="1.5"/><path d="M6.5 4.5 L10 8 L6.5 11.5" fill="none" stroke="var(--blue)" stroke-width="2"/></svg>Concrete Apron</li>
      <li><svg class="services__icon" viewBox="0 0 16 16"><circle cx="8" cy="8" r="7" fill="none" stroke="var(--blue)" stroke-width="1.5"/><path d="M6.5 4.5 L10 8 L6.5 11.5" fill="none" stroke="var(--blue)" stroke-width="2"/></svg>Concrete Sidewalk</li>
      <li><svg class="services__icon" viewBox="0 0 16 16"><circle cx="8" cy="8" r="7" fill="none" stroke="var(--blue)" stroke-width="1.5"/><path d="M6.5 4.5 L10 8 L6.5 11.5" fill="none" stroke="var(--blue)" stroke-width="2"/></svg>Concrete Patio</li>
    </ul>

    <p class="web">www.kestrel-paving.com and www.kestrel-masonry.com</p>
  </section>
</body>
</html>
```